Kestrel Bay Warehousing Group Needs A Website

We are looking for a website for a new company. 4 Pages

Needs to be responsive and mobile friendly for all browsers and coded for both Android & IOS. SEO is also important.

Website Brief – Kestrel Bay Warehousing Group
Domain: www.kestrelbaywarehousing.com
Email: info@kestrelbaywarehousing.com
Phone: to be inserted later
Address: 10458 82 Ave, Edmonton, AB T6E 2K9
Platform: WordPress (recommended for flexibility, SEO tools, and ease of editing)
Requirements:
• Responsive & mobile-friendly (Android & iOS)
• Cross-browser compatibility
• Fast page load speed
• SEO optimized for storage development, management, and investment keywords
• Easy in-house editing after launch
• Professional, modern, trust-driven design reflecting expertise, reliability, and innovation
________________________________________
Pages
1. HOME
Purpose: Quickly communicate who Kestrel Bay Warehousing Group is and why they’re the best choice for designing, building, leasing, and managing self storage facilities.
Content Highlights:
• Hero Section: Large, bold image of a modern self storage facility with headline:
"From Concept to Capacity – Your Self Storage Experts"
• Subheadline: “Kestrel Bay Warehousing Group delivers turnkey design, construction, leasing, and management services for profitable self storage operations.”
• Quick Service Icons:
o Facility Design & Development
o Construction & Build Management
o Lease-Up & Marketing
o Ongoing Facility Management
• Call to Action Button: “LEARN MORE” → links to ABOUT US page.
• Featured Project Highlights: Showcase a few completed or current projects with photos and stats.
• Contact Banner: “Ready to build your next self storage project? Let’s talk.” → CONTACT page.
2. ABOUT US
Purpose: Build credibility, showcase experience, and explain the value proposition.
Content Highlights:
• Who We Are: Overview of Kestrel Bay Warehousing Group’ history, mission, and team expertise.
• Our Approach: End-to-end process from site selection to occupancy.
• Why Choose Us:
o Industry expertise in self storage
o Proven track record in lease-up success
o Strong vendor and contractor network
3. SERVICES
Purpose: Detail all service offerings with clarity and authority.
Sections:
• Design & Development: Market analysis, site planning, and architectural design.
• Construction Management: Overseeing timelines, budgets, and quality control.
• Lease-Up Strategy: Marketing, promotions, and occupancy acceleration.
• Ongoing Facility Management: Staffing, maintenance, revenue optimization.

4. CONTACT
Purpose: Provide simple, direct ways to connect.
Content Highlights:
• Contact Form (Name, Email, Phone, Message)
• Direct Email: info@kestrelbaywarehousing.com
• Phone (if applicable)
• Google Map embed (if there’s a head office location)
• CTA: “Let’s Build Your Storage Success Story.”
Design & Technical Notes
• Visual Style: Clean, modern, bold typography, professional color palette (to be based on branding), strong imagery of self storage facilities.
• Performance: Image compression, caching, responsive scaling.
• SEO Targets: “Self storage facility developer,” “self storage construction,” “self storage management company,” “lease-up services for self storage.”

WordPress or Joomla – must be desktop and mobile friendly with fast page load speed. Need the ability to edit ourselves.

Use pantone colours - #033c5a – dark blue
#2baadf – light blue

```html
<!DOCTYPE html>
<html lang="en">
<head>
<meta charset="utf-8">
<title>Kestrel Bay Warehousing Group – Self Storage Experts</title>
<link href="https://fonts.googleapis.com/css2?family=Montserrat:wght@400;500;600;700;800&display=swap" rel="stylesheet">
<style>
:root{
  --navy:#033c5a;
  --sky:#2baadf;
  --ink:#1d2b36;
  --muted:#5d6b75;
  --line:#d7e4ec;
  --mist:#eef1f3;
  --white:#ffffff;
}
*{box-sizing:border-box;margin:0;padding:0}
html,body{width:1200px;height:2708px;overflow:hidden}
body{font-family:"Montserrat",Arial,sans-serif;color:var(--ink);background:var(--white);position:relative}
a{color:inherit;text-decoration:none}

/* header */
.site-header{position:absolute;top:0;left:0;width:1200px;height:80px;display:flex;align-items:center;padding:0 60px;background:var(--white)}
.brand{display:flex;align-items:center;gap:12px;width:300px}
.brand-mark{width:34px;height:34px;background:var(--navy);flex:none}
.brand-name{font-weight:700;font-size:15px;line-height:1.15;color:var(--navy);width:190px}
.main-nav{display:flex;margin-left:30px}
.main-nav a{font-size:13px;font-weight:600;color:var(--navy);padding:6px 26px;border-left:1px solid var(--line);letter-spacing:.5px}
.main-nav a:first-child{border-left:none}
.main-nav a.active{color:var(--sky);text-decoration:underline;text-underline-offset:8px;text-decoration-thickness:2px}
.header-email{margin-left:auto;display:flex;align-items:center;gap:8px;font-size:13px;font-weight:600;color:var(--navy)}
.header-email .ico{width:26px;height:26px;border-radius:4px;background:var(--navy);display:flex;align-items:center;justify-content:center}

/* hero */
.hero{position:absolute;top:80px;left:0;width:1200px;height:620px;background:linear-gradient(90deg,#cfd6db 0%,#f7f8f9 30%,#ffffff 50%,#f7f8f9 70%,#cfd6db 100%)}
.hero-copy{position:absolute;top:80px;left:0;width:1200px;text-align:center}
.hero-title{display:inline-block;font-weight:800;font-size:40px;line-height:1;text-transform:uppercase}
.hero-title span{display:block;padding:10px 24px;color:var(--white)}
.hero-title .l1{background:var(--navy)}
.hero-title .l2{background:var(--sky)}
.hero-sub{width:600px;margin:22px auto 0;font-size:17px;line-height:1.5;color:var(--navy);font-weight:500}
.btn{display:inline-block;font-weight:700;font-size:13px;letter-spacing:1px;padding:13px 28px;background:var(--sky);color:var(--white)}
.hero .btn{margin-top:24px}

/* services */
.services{position:absolute;top:700px;left:0;width:1200px;height:460px;background:var(--white);text-align:center}
.eyebrow{font-size:12px;font-weight:600;letter-spacing:2px;color:var(--sky);text-transform:uppercase}
.section-title{font-size:36px;font-weight:800;color:var(--navy);text-transform:uppercase;margin-top:4px}
.title-rule{width:60px;height:3px;background:var(--sky);margin:14px auto 0}
.services .eyebrow{margin-top:28px}
.service-grid{position:absolute;top:148px;left:140px;width:920px;height:200px;display:flex}
.service-card{flex:1;border:2px solid #bfe3f3;background:var(--white);display:flex;flex-direction:column;align-items:center;justify-content:center;gap:16px;padding:0 16px}
.service-card + .service-card{border-left:none}
.service-card h3{font-size:16px;font-weight:700;color:var(--navy);line-height:1.3}
.service-card.featured{background:var(--navy);border-color:var(--navy);margin:-24px 0;position:relative;z-index:1}
.service-card.featured h3{color:var(--white)}
.service-card.featured .btn{padding:10px 22px;font-size:11px}

/* projects */
.projects{position:absolute;top:1160px;left:0;width:1200px;height:732px;background:var(--mist);text-align:center}
.projects .eyebrow{margin-top:48px}
.project-grid{position:absolute;top:152px;left:130px;width:940px;display:flex;gap:40px;text-align:left}
.project-card{flex:1;background:var(--white);box-shadow:0 6px 18px rgba(3,60,90,.12)}
.project-photo{height:240px;background:linear-gradient(180deg,#aab7bf 0%,#dfe5e8 55%,#8a959b 100%)}
.project-photo.alt{background:linear-gradient(180deg,#bfc6cb 0%,#4a5a66 45%,#1f5b8c 100%)}
.project-body{padding:20px 26px 26px}
.project-body h4{font-size:20px;font-weight:700;color:var(--navy)}
.project-body p{font-size:13px;color:var(--muted);margin-top:6px;line-height:1.5}
.stats{display:flex;margin-top:20px;gap:12px}
.stat{flex:1;display:flex;gap:8px;align-items:flex-start}
.stat .dot{width:22px;height:22px;border-radius:50%;background:#d9eef8;flex:none}
.stat b{display:block;font-size:13px;color:var(--navy)}
.stat small{font-size:11px;color:var(--muted)}
.carousel-nav{position:absolute;top:620px;left:0;width:1200px;display:flex;justify-content:center;gap:14px}
.carousel-nav span{width:44px;height:44px;border-radius:50%;display:flex;align-items:center;justify-content:center}
.carousel-nav .prev{background:var(--sky)}
.carousel-nav .next{background:var(--navy)}

/* contact banner */
.contact-banner{position:absolute;top:1892px;left:0;width:1200px;height:488px;background:linear-gradient(90deg,#0a2f47 0%,#0c4c72 45%,#1873a6 100%);text-align:center;color:var(--white)}
.contact-banner .eyebrow{color:#bfe6f7;padding-top:82px}
.cta-frame{position:absolute;top:124px;left:240px;width:720px;height:240px;border:2px solid rgba(255,255,255,.85);display:flex;flex-direction:column;align-items:center;justify-content:center}
.cta-frame h2{font-size:36px;font-weight:800;line-height:1.2;text-transform:uppercase}
.cta-frame .btn{margin-top:24px;position:absolute;bottom:-22px}

/* footer */
.site-footer{position:absolute;top:2380px;left:0;width:1200px;height:260px;background:var(--white);display:flex;padding:42px 130px 0}
.footer-brand{width:260px}
.footer-brand .brand{width:auto}
.socials{display:flex;gap:10px;margin-top:28px}
.socials span{width:34px;height:34px;border-radius:50%;border:2px solid var(--sky)}
.socials span:first-child{background:var(--navy);border-color:var(--navy)}
.footer-col{padding:0 28px;border-left:1px solid var(--line);min-height:170px}
.footer-col h5{font-size:14px;font-weight:700;color:var(--navy);text-transform:uppercase;letter-spacing:.5px;margin-bottom:14px}
.footer-col li{list-style:none;font-size:13px;color:var(--muted);margin-bottom:7px}
.footer-col li::before{content:"•";color:var(--sky);margin-right:7px}
.footer-col.contact li::before{content:none}
.contact-line{display:flex;gap:10px;align-items:center;font-size:13px;color:var(--muted);margin-bottom:14px}
.contact-line .ico{width:26px;height:26px;border-radius:4px;background:var(--navy);display:flex;align-items:center;justify-content:center;flex:none}
.copyright{position:absolute;top:2640px;left:0;width:1200px;height:68px;border-top:1px solid var(--line);display:flex;align-items:center;justify-content:center;font-size:12px;color:var(--muted)}
</style>
</head>
<body>

<header class="site-header">
  <a class="brand" href="#"><span class="brand-mark"></span><span class="brand-name">Kestrel Bay Warehousing Group</span></a>
  <nav class="main-nav">
    <a class="active" href="#">HOME</a><a href="#">ABOUT US</a><a href="#">SERVICES</a><a href="#">CONTACT</a>
  </nav>
  <a class="header-email" href="mailto:info@kestrelbaywarehousing.com">
    <span class="ico"><svg width="14" height="10" viewBox="0 0 14 10"><rect x="0.5" y="0.5" width="13" height="9" fill="none" stroke="#fff"/><path d="M1 1l6 5 6-5" fill="none" stroke="#fff"/></svg></span>
    info@kestrelbaywarehousing.com
  </a>
</header>

<section class="hero" role="img" aria-label="Bright self storage corridor lined with white roll-up doors">
  <div class="hero-copy">
    <h1 class="hero-title"><span class="l1">From Concept to Capacity</span><span class="l2">Your Self Storage Experts</span></h1>
    <p class="hero-sub">Kestrel Bay Warehousing Group delivers turnkey design, construction, leasing, and management services for profitable self-storage operations.</p>
    <a class="btn" href="#">LEARN MORE ›</a>
  </div>
</section>

<section class="services">
  <p class="eyebrow">What we provide</p>
  <h2 class="section-title">Our Services</h2>
  <div class="title-rule"></div>
  <div class="service-grid">
    <div class="service-card">
      <svg width="44" height="44" viewBox="0 0 44 44" fill="none" stroke="#2baadf" stroke-width="2"><rect x="6" y="8" width="32" height="26"/><path d="M6 16h32M14 24h16M14 29h10M16 40h12M22 34v6"/></svg>
      <h3>Facility Design &amp; Development</h3>
    </div>
    <div class="service-card featured">
      <svg width="44" height="44" viewBox="0 0 44 44" fill="none" stroke="#2baadf" stroke-width="2"><path d="M6 38h32M10 38V18l12-8 12 8v20M16 38V26h12v12M16 30h12"/></svg>
      <h3>Construction &amp; Build Management</h3>
      <a class="btn" href="#">LEARN MORE ›</a>
    </div>
    <div class="service-card">
      <svg width="44" height="44" viewBox="0 0 44 44" fill="none" stroke="#2baadf" stroke-width="2"><path d="M8 26h8l14-10v24L16 30H8z"/><path d="M34 22h4M33 15l3-3M33 33l3 3"/></svg>
      <h3>Lease-Up &amp; Marketing</h3>
    </div>
    <div class="service-card">
      <svg width="44" height="44" viewBox="0 0 44 44" fill="none" stroke="#2baadf" stroke-width="2"><circle cx="22" cy="22" r="7"/><path d="M22 6v6M22 32v6M6 22h6M32 22h6M11 11l4 4M29 29l4 4M11 33l4-4M29 15l4-4"/></svg>
      <h3>Ongoing Facility Management</h3>
    </div>
  </div>
</section>

<section class="projects">
  <p class="eyebrow">Completed projects</p>
  <h2 class="section-title">Featured Projects</h2>
  <div class="title-rule"></div>
  <div class="project-grid">
    <article class="project-card">
      <div class="project-photo" role="img" aria-label="Exterior row of single-storey storage buildings with roll-up doors"></div>
      <div class="project-body">
        <h4>Project Heading</h4>
        <p>Drive-up units and wide lanes built for easy loading access.</p>
        <div class="stats">
          <div class="stat"><span class="dot"></span><div><b>10,000+</b><small>Storage units</small></div></div>
          <div class="stat"><span class="dot"></span><div><b>500,000 sq. ft.</b><small>Sq. footage space</small></div></div>
          <div class="stat"><span class="dot"></span><div><b>#1 Rated</b><small>Local self storage</small></div></div>
        </div>
      </div>
    </article>
    <article class="project-card">
      <div class="project-photo alt" role="img" aria-label="Open storage unit with a raised door revealing an empty interior"></div>
      <div class="project-body">
        <h4>Project Heading</h4>
        <p>Climate-controlled interior units with secure keypad entry.</p>
        <div class="stats">
          <div class="stat"><span class="dot"></span><div><b>10,000+</b><small>Storage units</small></div></div>
          <div class="stat"><span class="dot"></span><div><b>500,000 sq. ft.</b><small>Sq. footage space</small></div></div>
          <div class="stat"><span class="dot"></span><div><b>#1 Rated</b><small>Local self storage</small></div></div>
        </div>
      </div>
    </article>
  </div>
  <div class="carousel-nav">
    <span class="prev"><svg width="18" height="14" viewBox="0 0 18 14" fill="none" stroke="#fff" stroke-width="2"><path d="M17 7H2M7 1L1 7l6 6"/></svg></span>
    <span class="next"><svg width="18" height="14" viewBox="0 0 18 14" fill="none" stroke="#fff" stroke-width="2"><path d="M1 7h15M11 1l6 6-6 6"/></svg></span>
  </div>
</section>

<section class="contact-banner" role="img" aria-label="Hands reviewing building plans beside a blue-toned storage facility">
  <p class="eyebrow">Get in touch with us</p>
  <div class="cta-frame">
    <h2>Ready to build your next self<br>storage project?<br>Let’s talk.</h2>
    <a class="btn" href="#">CONTACT US ›</a>
  </div>
</section>

<footer class="site-footer">
  <div class="footer-brand">
    <a class="brand" href="#"><span class="brand-mark"></span><span class="brand-name">Kestrel Bay Warehousing Group</span></a>
    <div class="socials"><span></span><span></span><span></span><span></span></div>
  </div>
  <div class="footer-col">
    <h5>Navigation</h5>
    <ul><li>Home</li><li>About Us</li><li>Service</li><li>Contact us</li></ul>
  </div>
  <div class="footer-col">
    <h5>Services</h5>
    <ul><li>Design &amp; Development</li><li>Construction Management</li><li>Lease-Up Strategy</li><li>Ongoing Facility Management</li></ul>
  </div>
  <div class="footer-col contact">
    <h5>Contact Us</h5>
    <div class="contact-line"><span class="ico"><svg width="14" height="10" viewBox="0 0 14 10"><rect x="0.5" y="0.5" width="13" height="9" fill="none" stroke="#fff"/><path d="M1 1l6 5 6-5" fill="none" stroke="#fff"/></svg></span>info@kestrelbaywarehousing.com</div>
    <div class="contact-line"><span class="ico"><svg width="12" height="14" viewBox="0 0 12 14"><path d="M6 13S1 8 1 5a5 5 0 0110 0c0 3-5 8-5 8z" fill="none" stroke="#fff"/><circle cx="6" cy="5" r="1.6" fill="#fff"/></svg></span>10458 82 Ave, Edmonton,<br>AB T6E 2K9</div>
    <div class="contact-line"><span class="ico"><svg width="14" height="14" viewBox="0 0 14 14"><circle cx="7" cy="7" r="6" fill="none" stroke="#fff"/><path d="M1 7h12M7 1c3 3 3 9 0 12M7 1c-3 3-3 9 0 12" fill="none" stroke="#fff"/></svg></span>www.kestrelbaywarehousing.com</div>
  </div>
</footer>
<div class="copyright">Copyright © 2025 Kestrel Bay Warehousing Group. All Rights Reserved</div>

</body>
</html>
```